Saliva drug test label design "VeloTest K4"

Hello everyone. We need a saliva drug test sticker designed. We need the VeloTest brand with "K4" after... eg VeloTst K4.

Also, the current design in the example stencil will need to be updated to a more modern design, but still needs ID:, Date:, peel label line with description, etc.

Target Market(s)

high safety workplaces, mine sites, construction, etc

Industry/Entity Type

construction, aviation, mining, transport, etc

Colors

Designer to choose colors to be used in the design.

Requirements
Must have
• VeloTest K4 as the logo, interpret results negative, positive, and invalid picture.

```html
<!DOCTYPE html>
<html lang="en">
<head>
<meta charset="utf-8">
<title>VeloTest K4 – Oral Fluid Drug Test Labels</title>
<link href="https://fonts.googleapis.com/css2?family=Roboto+Condensed:wght@300;400;500;700&family=Roboto:wght@400&display=swap" rel="stylesheet">
<style>
  :root{
    --bg:#d3e9ef;
    --paper:#ffffff;
    --brand:#1c9ad6;
    --pill:#8c8c8c;
    --accent:#e8522a;
    --strip:#2a8fd0;
    --ink:#1b1b1b;
    --chevron:#c9c9c9;
    --band-top:#e6f0f9;
    --band-mid:#b9d4ee;
  }
  *{margin:0;padding:0;box-sizing:border-box}
  html,body{width:845px;height:1200px;overflow:hidden}
  body{background:var(--bg);position:relative;font-family:"Roboto Condensed",sans-serif;color:var(--ink)}
  h2{font-weight:400}

  .label{position:absolute;background:var(--paper);box-shadow:6px 10px 18px rgba(60,90,110,.25)}

  /* front label */
  .label--front{left:146px;top:400px;width:224px;height:400px;border-radius:12px;overflow:hidden}
  .brand{position:absolute;left:0;right:0;text-align:center;font-weight:700;color:var(--brand);white-space:nowrap}
  .label--front .brand{top:35px;font-size:28px;letter-spacing:-.3px}
  .brand-dot{display:inline-block;width:10px;height:10px;border-radius:50%;background:currentColor;margin-left:6px;vertical-align:middle}
  .pill{position:absolute;left:18px;top:81px;width:186px;height:26px;border-radius:13px;background:var(--pill);color:#fff;font-weight:700;font-size:15px;line-height:26px;text-align:center}
  .wave{position:absolute;left:0;right:0;top:120px;height:77px;background:linear-gradient(180deg,#fff 0%,var(--band-top) 25%,var(--band-mid) 50%,var(--band-top) 75%,#fff 100%)}
  .results-title{position:absolute;left:0;right:0;top:209px;text-align:center;color:var(--accent);font-size:20px;line-height:26px}
  .results{position:absolute;left:0;top:249px;width:224px;height:50px}
  .result-names{position:absolute;top:299px;left:0;width:224px;font-size:15px;line-height:20px}
  .result-names span{position:absolute;transform:translateX(-50%)}
  .sample-port{position:absolute;left:17px;top:370px;font-size:13.5px;line-height:18px;font-weight:300;letter-spacing:0;display:flex;align-items:center;gap:4px}
  .sample-port svg{width:12px;height:9px}

  /* seal label */
  .label--seal{left:456px;top:566px;width:280px;height:234px;border-radius:6px;overflow:hidden}
  .seal-head{height:46px;background:var(--brand);position:relative}
  .label--seal .brand{color:#fff;top:11px;font-size:21px}
  .seal-title{position:absolute;left:0;right:0;top:62px;text-align:center;font-size:23px;line-height:28px}
  .field{position:absolute;left:32px;color:var(--brand);font-family:"Roboto",sans-serif;font-size:21px;line-height:26px;display:flex;align-items:baseline}
  .field b{font-weight:400;width:52px}
  .field i{font-style:normal;width:12px}
  .field--id{top:102px}
  .field--date{top:136px}
  .field-line{position:absolute;left:100px;width:148px;height:2px;background:var(--brand)}
  .field-line--id{top:122px}
  .field-line--date{top:156px}
  .peel{position:absolute;left:0;right:0;top:188px;text-align:center;font-family:"Roboto",sans-serif;font-size:12px;line-height:12px}
  .chevrons{position:absolute;top:194px;width:52px;height:26px}
  .chevrons--left{left:2px}
  .chevrons--right{right:2px}
</style>
</head>
<body>

<section class="label label--front" aria-label="Device front label">
  <div class="brand">VeloTest K4<span class="brand-dot"></span></div>
  <div class="pill">Oral Fluid Drug Test</div>
  <div class="wave" role="img" aria-label="Decorative blue wave band area"></div>
  <h2 class="results-title">INTERPRET RESULTS</h2>
  <svg class="results" viewBox="0 0 224 50" aria-hidden="true">
    <g font-family="Roboto Condensed, sans-serif" font-size="14" font-weight="700" fill="#1b1b1b">
      <text x="24" y="17">C</text><text x="24" y="40">T</text>
      <text x="97" y="17">C</text><text x="97" y="40">T</text>
      <text x="147" y="17">C</text><text x="147" y="40">T</text>
    </g>
    <g fill="none" stroke="#2a8fd0" stroke-width="1.2">
      <rect x="37" y="1" width="15" height="46" rx="2"/>
      <rect x="57" y="1" width="15" height="46" rx="2"/>
      <rect x="109" y="1" width="15" height="46" rx="2"/>
      <rect x="159" y="1" width="15" height="46" rx="2"/>
      <rect x="180" y="1" width="15" height="46" rx="2"/>
    </g>
    <g stroke="#e02020" stroke-width="2.2">
      <line x1="37" y1="12" x2="52" y2="12"/><line x1="57" y1="12" x2="72" y2="12"/>
      <line x1="37" y1="35" x2="52" y2="35"/><line x1="57" y1="35" x2="72" y2="35"/>
      <line x1="109" y1="12" x2="124" y2="12"/>
      <line x1="159" y1="35" x2="174" y2="35"/>
    </g>
  </svg>
  <div class="result-names">
    <span style="left:55px">Negative</span>
    <span style="left:116px">Positive</span>
    <span style="left:174px">Invalid</span>
  </div>
  <div class="sample-port">
    <svg viewBox="0 0 12 9" aria-hidden="true"><path d="M0 0H12L6 9Z" fill="#e8522a"/></svg>
    SAMPLE PORT AT THE BOTTOM
  </div>
</section>

<section class="label label--seal" aria-label="Seal label">
  <div class="seal-head"><div class="brand">VeloTest K4<span class="brand-dot"></span></div></div>
  <h2 class="seal-title">Oral Fluid Drug Test</h2>
  <div class="field field--id"><b>ID</b><i>:</i></div>
  <div class="field-line field-line--id"></div>
  <div class="field field--date"><b>Date</b><i>:</i></div>
  <div class="field-line field-line--date"></div>
  <svg class="chevrons chevrons--left" viewBox="0 0 52 26" aria-hidden="true">
    <g fill="#c9c9c9"><path d="M14 0h8L12 13l10 13h-8L4 13Z"/><path d="M28 0h8L26 13l10 13h-8L18 13Z"/><path d="M42 0h8L40 13l10 13h-8L32 13Z"/></g>
  </svg>
  <p class="peel">Peel label to ensure oral fluid<br>touches bottom of test strips.<br>Keep test device upright.</p>
  <svg class="chevrons chevrons--right" viewBox="0 0 52 26" aria-hidden="true">
    <g fill="#c9c9c9"><path d="M14 0h8L12 13l10 13h-8L4 13Z"/><path d="M28 0h8L26 13l10 13h-8L18 13Z"/><path d="M42 0h8L40 13l10 13h-8L32 13Z"/></g>
  </svg>
</section>

</body>
</html>
```